Home page web design for "Tales from Thee"

We need a home page web design for a start up company that will write memoirs for seniors.
The completed project will need to include PSD files...NO HTML or CSS necessary.
Attached is a brief outline concept that may give you some ideas...but you are the creative professionals, so please feel free to add your ideas. We will also attach some files that show you our logo, brochures, and photos that could be used to give you ideas of our focus.
There will need to be access to the other pages on the home page to include: 'About Us'; 'How We Can Help'; 'Community Sessions'; 'Senior Consulting ' and 'Contact Us'.
Updates

Target Market(s)

Seniors and Baby Boomers

Industry/Entity Type

It Company

Number of Pages Required

1 page

Colors
f9ba93
fbca95
faa54b
faf289
f37123

Requirements
Must have
• Script easy on senior eyes.
• Initial contact number would be 844-4LANTERN
Nice to have
• While the color pallet is non-specific we prefer the warm colors.
• salmon, peach.......
• NOT so much the orange of Halloween:)
• However, please utilize your creativity and put in colors you feel will draw best with your design.

```html
<!DOCTYPE html>
<html lang="en">
<head>
<meta charset="utf-8">
<title>Tales from Thee — Home</title>
<link href="https://fonts.googleapis.com/css2?family=Ubuntu:wght@400;500&family=Nunito+Sans:wght@400;600&display=swap" rel="stylesheet">
<style>
:root{
  --ink:#3d3a36;
  --muted:#5d5a55;
  --tan:#b8a16c;
  --tan-dark:#9a8456;
  --tan-text:#a88f5e;
  --footer-ink:#4a3f2c;
  --orange:#f8a54b;
  --peach:#fbca95;
  --pumpkin:#f37123;
  --gold:#f2c21c;
  --white:#ffffff;
}
*{box-sizing:border-box;margin:0;padding:0}
html,body{width:757px;height:1200px;overflow:hidden;background:#fff}
body{position:relative;font-family:"Nunito Sans",Arial,sans-serif;color:var(--ink)}
.abs{position:absolute}
.header{left:0;top:0;width:757px;height:94px;background:#f8f8f7}
.brand{left:84px;top:24px;width:148px;height:46px;display:flex;align-items:center;gap:7px;font-family:"Ubuntu",sans-serif;font-size:15px;color:var(--tan-text)}
.brand .mark{width:12px;height:12px;border-radius:50%;background:var(--tan)}
.call-label{left:608px;top:20px;font-size:8px;color:var(--muted)}
.phone{left:608px;top:33px;font-size:11.5px;color:var(--tan-text);font-weight:600}
.email{left:571px;top:60px;font-size:8px;color:var(--muted)}
.nav{left:0;top:94px;width:757px;height:35px;background:linear-gradient(#bea776,#ad9562)}
.nav a{position:absolute;top:0;height:35px;line-height:35px;font-size:9.5px;color:#fff;text-decoration:none}
.nav a.active{background:var(--tan-dark);padding:0 13px}
.hero{left:0;top:129px;width:757px;height:296px;background:linear-gradient(180deg,#8a8480 0%,#6b5a4e 45%,#4a3b33 100%)}
.hero-title{font-family:"Ubuntu",sans-serif;color:#fff;background:rgba(45,42,40,.85);height:26px;line-height:26px;text-align:center;font-size:19px}
.hero-sub{left:398px;top:279px;width:265px;text-align:center;color:var(--gold);font-family:"Ubuntu",sans-serif;font-weight:500;font-size:12px}
.hero-body{left:392px;top:297px;width:278px;text-align:center;color:#fff;font-size:8.6px;line-height:15.5px}
.dots{left:494px;top:358px;width:66px;height:17px;border-radius:3px;background:rgba(40,36,33,.8);display:flex;justify-content:center;align-items:center;gap:4px}
.dots i{width:8px;height:8px;border-radius:50%;background:#111}
.dots i:first-child{background:#c8ad6a}
h2{font-family:"Ubuntu",sans-serif;font-weight:400}
.about-h{left:83px;top:466px;font-size:18px;color:var(--ink)}
.about-h span,.accent{color:var(--pumpkin)}
.copy{font-size:8px;line-height:16px;color:var(--muted)}
.help{left:0;top:635px;width:757px;height:268px;background:var(--orange)}
.help-h{left:82px;top:671px;font-size:16.5px;color:#fff}
.help-list{left:83px;top:705px;width:189px;color:#fff;font-size:8px;line-height:15px}
.help-list p{padding:2px 0 8px;border-bottom:1px solid rgba(255,255,255,.35);margin-bottom:9px}
.help-list p.last{border:0;margin-bottom:6px}
.pkg{top:670px;width:113px;height:196px;background:var(--peach);text-align:center}
.pkg h3{font-family:"Ubuntu",sans-serif;font-weight:400;font-size:13px;margin-top:14px;color:var(--ink)}
.pkg p{font-size:8px;line-height:15.2px;color:var(--muted);margin:14px 14px 0}
.btn{position:absolute;left:21px;top:155px;width:70px;height:25px;line-height:25px;background:var(--pumpkin);color:#fff;font-size:8px}
.comm-h{left:363px;top:947px;font-size:16px;color:var(--ink)}
.comm-h span{color:#c49f66}
.footer{left:0;top:1108px;width:757px;height:92px;background:linear-gradient(#bea776,#b19b66)}
.footer-links{left:83px;font-size:8px;line-height:12px;color:var(--footer-ink);white-space:nowrap}
.copyright{left:83px;top:1173px;font-size:8px;line-height:12px;color:#fff;white-space:nowrap}
.follow{left:566px;top:1130px;font-size:10px;color:#fff}
</style>
</head>
<body>
<div class="abs header"></div>
<div class="abs brand"><span class="mark"></span>Tales from Thee</div>
<svg class="abs" style="left:590px;top:21px" width="11" height="11" viewBox="0 0 11 11"><rect width="11" height="11" rx="2" fill="#b8a16c"/><path d="M3.5 2.5l1.3 1.6-.8.9c.4.9 1 1.5 1.9 1.9l.9-.8 1.6 1.3-.8 1.1C5.3 8.3 2.8 5.7 2.4 3.3z" fill="#fff"/></svg>
<div class="abs call-label">Call Us Now</div>
<div class="abs phone">844-4LANTERN</div>
<svg class="abs" style="left:555px;top:62px" width="10" height="7" viewBox="0 0 10 7"><rect width="10" height="7" fill="#b8a16c"/><path d="M0 0l5 4 5-4" stroke="#fff" fill="none" stroke-width=".8"/></svg>
<div class="abs email">Email : hello@talesfromthee.example</div>

<nav class="abs nav">
  <a class="active" style="left:82px">Home</a>
  <a style="left:150px">About us</a>
  <a style="left:213px">How We Can Help</a>
  <a style="left:314px">Community Services</a>
  <a style="left:426px">Senior Consulting Services</a>
  <a style="left:561px">Contact us</a>
</nav>

<div class="abs hero" role="img" aria-label="Photo of an elderly couple walking along a beach at dusk"></div>
<div class="abs hero-title" style="left:445px;top:195px;width:184px">Ordinary Lives......</div>
<div class="abs hero-title" style="left:416px;top:233px;width:238px">Extraordinary Legacies</div>
<div class="abs hero-sub">When a genealogy doesn’t say enough!</div>
<div class="abs hero-body">If you were alive in 100 years, what would you share with your descendants? Now you have a vehicle to help you immortalize your thoughts for the future.</div>
<div class="abs dots"><i></i><i></i><i></i><i></i></div>

<h2 class="abs about-h">About <span>Us</span></h2>
<div class="abs copy" style="left:83px;top:495px;width:360px">
  <p style="width:340px">We are not all presidents of countries or CEO’s of fortune 500 companies! But “every life legacy is a gift to be treasured by the next generation.”</p>
  <p style="margin-top:16px">Does your family host generations of soldiers, doctors, farmers, scientists, mechanics, entrepreneurs, writers, politicians, contractors, pastors, artisans, athletes, musicians, etc..? Generational patterns can often emerge when writing your story that will interest the next generation. <span class="accent">&nbsp;[ Read More ]</span></p>
</div>
<div class="abs" style="left:463px;top:480px;width:208px;height:122px;background:linear-gradient(135deg,#3a1f12,#8a5a30 50%,#c9a27a)" role="img" aria-label="Photo of an elderly woman writing by lamplight at a desk"></div>

<div class="abs help"></div>
<h2 class="abs help-h">How We Can Help?</h2>
<div class="abs help-list">
  <p>A genealogy, while very relevant, doesn’t offer the personal story of the names we find.</p>
  <p>Every life is a legacy to pass forward and we at Tales from Thee believe everyone should chronicle their life journey in writing.</p>
  <p class="last">Do you know the triumphs and tribulations of your ancestors? Do you wish you did?</p>
  <div>[ Read More ]</div>
</div>
<div class="abs pkg" style="left:304px"><h3>Package 1</h3><p>Generational pat-terns can often emerge when writing your story that will interest the next generation.</p><span class="btn">Learn More</span></div>
<div class="abs pkg" style="left:431px"><h3>Package 2</h3><p>Generational pat-terns can often emerge when writing your story that will interest the next generation.</p><span class="btn">Learn More</span></div>
<div class="abs pkg" style="left:560px"><h3>Package 3</h3><p>Generational pat-terns can often emerge when writing your story that will interest the next generation.</p><span class="btn">Learn More</span></div>

<div class="abs" style="left:83px;top:933px;width:257px;height:137px;background:linear-gradient(180deg,#eee9e4,#c9b6b0 40%,#8e9ab0 80%,#e8e4e0)" role="img" aria-label="Photo of a smiling group of seniors standing together"></div>
<h2 class="abs comm-h"><span>Community</span> Session</h2>
<div class="abs copy" style="left:363px;top:977px;width:290px;line-height:15.2px">A genealogy, while very relevant, doesn’t offer the personal story of the names we find. A biography can place a deeper relevance on the face for future descendants. Every life is a legacy to pass forward and we at Tales from Thee believe everyone should chronicle their life journey in writing. This commitment allows you to be remembered for who you truly are as a person.</div>

<footer class="abs footer"></footer>
<div class="abs footer-links" style="top:1126px">Home &nbsp;| &nbsp;About us &nbsp;| &nbsp;How We Can Help &nbsp;| &nbsp;Community Services</div>
<div class="abs footer-links" style="top:1146px">Senior Consulting Services &nbsp;| &nbsp;Contact us</div>
<div class="abs copyright">Copyright © 2014. Tales from Thee &nbsp;All rights reserved.</div>
<div class="abs follow">Follow Us</div>
<svg class="abs" style="left:564px;top:1151px" width="110" height="20" viewBox="0 0 110 20" aria-label="Social links">
  <circle cx="10" cy="10" r="9.5" fill="#fff"/><circle cx="32.5" cy="10" r="9.5" fill="#fff"/><circle cx="55" cy="10" r="9.5" fill="#fff"/><circle cx="77.5" cy="10" r="9.5" fill="#fff"/><circle cx="100" cy="10" r="9.5" fill="#fff"/>
</svg>
</body>
</html>
```